Book Cover for Productivity Book

I need a book cover for my latest publication "On Momentum: The Gathered Insights of the Busiest Woman Living"

You can see my branding at www.brightmarrow.example

This is meant to be my epic pinaccle work on productivity, I want it to look like the end all be all word on productivity.

Target Market(s)

entrepreneurs

```html
<!DOCTYPE html>
<html lang="en">
<head>
<meta charset="utf-8">
<title>On Momentum – Book Cover</title>
<link href="https://fonts.googleapis.com/css2?family=Oranienbaum&display=swap" rel="stylesheet">
<style>
  :root {
    --page-bg: #ffffff;
    --cover-top: #2a2d33;
    --cover-mid: #1b1d21;
    --cover-bottom: #0b0b0d;
    --accent-red: #c8202a;
    --title-white: #ffffff;
    --portrait-light: rgba(70, 74, 82, 0.45);
    --portrait-dark: rgba(20, 21, 24, 0);
  }
  html, body {
    margin: 0;
    padding: 0;
    width: 1200px;
    height: 912px;
    overflow: hidden;
    background: var(--page-bg);
  }
  .canvas {
    position: relative;
    width: 1200px;
    height: 912px;
  }
  .book-cover {
    position: absolute;
    left: 36px;
    top: 30px;
    width: 600px;
    height: 800px;
    overflow: hidden;
    background: linear-gradient(180deg, var(--cover-top) 0%, var(--cover-mid) 45%, var(--cover-bottom) 100%);
    font-family: "Oranienbaum", "Times New Roman", serif;
  }
  .author-portrait {
    position: absolute;
    left: 360px;
    top: 270px;
    width: 260px;
    height: 520px;
    background: radial-gradient(ellipse at 45% 30%, var(--portrait-light) 0%, var(--portrait-dark) 70%);
  }
  .cover-title {
    margin: 0;
    font-weight: 400;
  }
  .title-lead,
  .title-main {
    position: absolute;
    display: block;
    white-space: nowrap;
    transform-origin: left top;
  }
  .title-lead {
    left: 88px;
    top: -2px;
    font-size: 104px;
    line-height: 1;
    color: var(--title-white);
    text-transform: uppercase;
    transform: scaleX(0.82);
  }
  .title-main {
    left: 28px;
    top: 86px;
    font-size: 178px;
    line-height: 1;
    color: var(--accent-red);
    letter-spacing: -2px;
    transform: scaleX(0.64);
  }
  .subtitle {
    position: absolute;
    left: 30px;
    top: 340px;
    margin: 0;
    padding: 0;
    list-style: none;
    color: var(--title-white);
    font-size: 56px;
    line-height: 78px;
    white-space: nowrap;
    transform: scaleX(0.8);
    transform-origin: left top;
  }
  .subtitle .initial {
    color: var(--accent-red);
  }
  .base-band {
    position: absolute;
    left: 0;
    bottom: 0;
    width: 100%;
    height: 13px;
    background: var(--accent-red);
  }
</style>
</head>
<body>
  <main class="canvas">
    <section class="book-cover" aria-label="Book cover: On Momentum">
      <div class="author-portrait" role="img" aria-label="Faded portrait photograph of the author in a dark t-shirt"></div>
      <h1 class="cover-title">
        <span class="title-lead">On</span>
        <span class="title-main">Momentum</span>
      </h1>
      <ul class="subtitle">
        <li><span class="initial">T</span>he</li>
        <li><span class="initial">G</span>athered Insights</li>
        <li><span class="initial">o</span>f the</li>
        <li><span class="initial">B</span>usiest Woman</li>
        <li><span class="initial">L</span>iving</li>
      </ul>
      <div class="base-band"></div>
    </section>
  </main>
</body>
</html>
```